Creative designs Needed! Dieting Tips for Nurses

Need a creative design for my first book that is targeted to nurses that want to lose weight.
THE TITLE OF MY BOOK IS:
The Bright Lantern Pantry Uprising:
9 Slim-Down Tricks Each Caregiver Should Learn!

- My audience is female.

- My colors for my business are red, black, gray and white however feel free to use other colors

- The cover should note there is Free Bonus Content.

- The book cover should have a fun modern feel to it.

- Since the title is talking about time. I think there should be some sort of clock in the design. Not an actual clock but a clock design.

- Please let me know if you need anything from me to complete your design. I go by Coach Brin.

- Subject of book is dieting tips for nurses

Target Market(s)

Nurses

Industry/Entity Type

Health And Wellness

Font styles to use
Serif

Colors
ec1f27
1b1b1b
dddddd

Requirements
Must have
• List the Free Bonus Content label on the front cover
• Must keep in mind there will be sequels to this book for other target markets
• • Should be creative, modern
• • Please try not to use stock images with just the text for this design - I am looking for something creative and unique.
• • Something that plays with the idea of time, think clock.
• • Need something out the box!!
• • Think diversity in the people if you do opt to use images - Would prefer if you steer clear of regular photos of people
• • If you do use an image of a nurse, please note nurses mostly wear scrubs today - so think about that in your concepts
Nice to have
• The design should be clever
Should not have
• Although I selected the 3 colors feel free to explore other colors and those 3 colors do not have to be the dominate colors.
• The book design should pop out to people when they see it.

```html
<!DOCTYPE html>
<html lang="en">
<head>
<meta charset="utf-8">
<title>The Bright Lantern Pantry Uprising – Book Cover</title>
<link rel="stylesheet" href="https://fonts.googleapis.com/css2?family=Montserrat:wght@700;900&family=Questrial&display=swap">
<style>
  :root {
    --brand-red: #e51d26;
    --ink: #111111;
    --silver-light: #f3f3f3;
    --silver-mid: #d8d8d8;
    --silver-dark: #bcbcbc;
    --white: #ffffff;
    --room-light: #f1ece8;
    --scrubs-blue: #3cb4e2;
    --scrubs-pale: #8fd2ee;
    --skin-warm: #d9b39a;
    --top-white: #f7f4f1;
    --cap-cream: #f5ecd2;
  }
  * { margin: 0; padding: 0; box-sizing: border-box; }
  html, body { width: 798px; height: 1200px; overflow: hidden; background: var(--white); }
  .cover {
    position: relative;
    width: 798px;
    height: 1200px;
    overflow: hidden;
    font-family: "Questrial", sans-serif;
    color: var(--ink);
  }
  .title-panel {
    position: absolute;
    left: 0; right: 0; top: 0; height: 622px;
    background: radial-gradient(ellipse at 50% 40%, var(--silver-light) 0%, var(--silver-mid) 65%, var(--silver-dark) 100%);
  }
  .title-row {
    position: absolute;
    left: 0; right: 0;
    display: flex;
    justify-content: center;
    align-items: baseline;
    white-space: nowrap;
  }
  .title-row--top { top: 8px; gap: 12px; }
  .title-small { font-size: 32px; line-height: 1; }
  .title-big { font-size: 96px; line-height: 1.2; letter-spacing: -1px; }
  .headline-red {
    font-family: "Montserrat", sans-serif;
    font-weight: 900;
    color: var(--brand-red);
    text-transform: uppercase;
    line-height: 1;
  }
  .title-row--uprising { top: 118px; }
  .title-row--uprising .headline-red { font-size: 142px; }
  .title-row--tricks { top: 244px; font-size: 58px; line-height: 1; }
  .title-row--caregiver { top: 325px; }
  .title-row--caregiver .headline-red {
    font-size: 124px;
    letter-spacing: -2px;
    transform: scaleY(1.98);
    transform-origin: top center;
  }
  .nurse-cap {
    position: absolute;
    left: 496px; top: 322px;
    width: 96px; height: 66px;
  }
  .closing-row {
    position: absolute;
    left: 28px; top: 550px;
    display: flex; align-items: baseline; gap: 22px;
    white-space: nowrap;
  }
  .closing-text { font-size: 70px; line-height: 1; }
  .author-name {
    font-family: "Montserrat", sans-serif;
    font-weight: 700;
    font-size: 34px;
    color: var(--brand-red);
  }
  .divider {
    position: absolute; left: 0; right: 0; top: 622px; height: 12px;
    background: var(--brand-red);
  }
  .photo-area {
    position: absolute; left: 0; right: 0; top: 634px; height: 488px;
    background: var(--room-light);
  }
  .photo-nurse {
    position: absolute; left: 0; top: 0; width: 470px; height: 100%;
    background: linear-gradient(180deg, var(--room-light) 0%, var(--scrubs-pale) 35%, var(--scrubs-blue) 70%, var(--scrubs-blue) 100%);
  }
  .photo-waist {
    position: absolute; left: 470px; top: 0; width: 328px; height: 100%;
    background: linear-gradient(180deg, var(--skin-warm) 0%, var(--top-white) 25%, var(--top-white) 62%, var(--skin-warm) 78%, var(--skin-warm) 100%);
  }
  .bonus-band {
    position: absolute; left: 0; right: 0; bottom: 0; height: 78px;
    background: var(--brand-red);
    display: flex; align-items: center; justify-content: center;
    color: var(--white);
    font-size: 46px;
    letter-spacing: 1px;
    white-space: nowrap;
  }
  .bonus-band strong { font-family: "Montserrat", sans-serif; font-weight: 900; margin-right: 14px; }
</style>
</head>
<body>
<main class="cover">
  <section class="title-panel">
    <div class="title-row title-row--top">
      <span class="title-small">THE BRIGHT</span>
      <span class="title-big">LANTERN</span>
      <span class="title-small">PANTRY</span>
    </div>
    <div class="title-row title-row--uprising"><span class="headline-red">UPRISING</span></div>
    <div class="title-row title-row--tricks">9 SLIM-DOWN TRICKS EACH</div>
    <div class="title-row title-row--caregiver"><span class="headline-red">CAREGIVER</span></div>
    <svg class="nurse-cap" viewBox="0 0 96 66" role="img" aria-label="Small nurse cap illustration with a red cross, resting on the headline">
      <rect x="0" y="0" width="96" height="66" rx="8" fill="var(--cap-cream)"/>
    </svg>
    <div class="closing-row">
      <span class="closing-text">SHOULD LEARN!</span>
      <span class="author-name">Coach Brin</span>
    </div>
  </section>
  <div class="divider"></div>
  <section class="photo-area">
    <div class="photo-nurse" role="img" aria-label="Photo of a smiling nurse in blue scrubs with a stethoscope and folded arms"></div>
    <div class="photo-waist" role="img" aria-label="Photo of a woman in a white sports top measuring her waist with a tape measure"></div>
  </section>
  <footer class="bonus-band"><strong>FREE</strong>BONUS CONTENT INSIDE!</footer>
</main>
</body>
</html>
```